Lakeshore Youngsters Circle Business Card Project

We are a Minneapolis based discount club that caters to families with children. We need a business card that can be used to communicate our contact information to other businesses that may wish to offer discounts on our website.

Please use placeholders for contact information (i.e. John Doe, 123 Any Street, Any Town, etc.) and include spaces for the following: Full name, title, email, phone number, website, one line street address, city, state, and zip code.
Updates

Reason: I have extended the deadline because I had not intended the project to close so quickly.

Target Market(s)

Most of the time the business cards will be used in business to business situations. However, from time to time they may be distributed to our end customer, families with children.

Industry/Entity Type

Club

Font styles to use
Serif
Sans Serif
Other font styles liked:
• Open to suggestions

Requirements
Nice to have
• We might use the reverse side of the card as the design for our membership card.

```html
<!DOCTYPE html>
<html lang="en">
<head>
<meta charset="utf-8">
<title>Lakeshore Youngsters Circle – Business Cards</title>
<link rel="stylesheet" href="https://fonts.googleapis.com/css2?family=Arimo:wght@400;700&display=swap">
<style>
  :root {
    --stage: #574840;
    --card-light: #ffffff;
    --card-dark: #424242;
    --name-red: #c8102e;
    --title-blue: #1f3f8f;
    --title-gold: #f2b51d;
    --text-dark: #333333;
    --text-light: #eeeeee;
    --rule: #c9c9c9;
    --brand-orange: #f39c1b;
    --stroke-orange: #f6a623;
    --stroke-blue: #1d2f85;
    --stroke-red: #c8202a;
    --stroke-green: #7fbf2a;
  }
  * { box-sizing: border-box; margin: 0; padding: 0; }
  html, body { width: 1200px; height: 694px; overflow: hidden; }
  body {
    background: var(--stage);
    font-family: "Arimo", Arial, sans-serif;
  }
  .sheet { position: relative; width: 1200px; height: 694px; }

  .card {
    position: absolute;
    width: 520px;
    height: 292px;
    overflow: hidden;
    background: var(--card-light);
  }
  .card--dark { background: var(--card-dark); }
  .card--front-light { left: 57px;  top: 55px; }
  .card--back-light  { left: 643px; top: 55px; }
  .card--front-dark  { left: 57px;  top: 361px; }
  .card--back-dark   { left: 643px; top: 361px; }

  /* brush stroke areas */
  .stroke { position: absolute; border-radius: 50%; }
  .stroke--orange-top {
    right: -10px; top: -22px; width: 240px; height: 60px;
    background: radial-gradient(ellipse at center, var(--stroke-orange) 0%, rgba(246,166,35,.55) 55%, rgba(246,166,35,0) 72%);
    transform: rotate(-6deg);
  }
  .stroke--blue-corner {
    left: -40px; bottom: -30px; width: 230px; height: 90px;
    background: radial-gradient(ellipse at center, var(--stroke-blue) 0%, rgba(29,47,133,.55) 50%, rgba(29,47,133,0) 72%);
    transform: rotate(18deg);
  }
  .stroke--red-corner {
    right: -20px; bottom: -30px; width: 310px; height: 110px;
    background: radial-gradient(ellipse at center, var(--stroke-red) 0%, rgba(200,32,42,.55) 50%, rgba(200,32,42,0) 72%);
    transform: rotate(-18deg);
  }
  .stroke--green-corner {
    right: -20px; bottom: -30px; width: 260px; height: 120px;
    background: radial-gradient(ellipse at center, var(--stroke-green) 0%, rgba(127,191,42,.55) 50%, rgba(127,191,42,0) 72%);
    transform: rotate(-24deg);
  }

  /* contact side */
  .holder { position: absolute; left: 38px; top: 76px; }
  .holder__name { font-size: 19px; font-weight: 400; color: var(--name-red); line-height: 1.1; }
  .holder__title { font-size: 11px; color: var(--title-blue); margin-top: 3px; }
  .card--dark .holder__title { color: var(--title-gold); }
  .holder__rule { width: 150px; height: 1px; background: var(--rule); margin-top: 14px; }
  .card--dark .holder__rule { background: #6a6a6a; }

  .contact { position: absolute; left: 30px; top: 164px; font-size: 10px; line-height: 15.5px; color: var(--text-dark); }
  .card--dark .contact { color: var(--text-light); }
  .contact__row { display: flex; }
  .contact__label { width: 76px; text-align: right; padding-right: 4px; }
  .contact__web { margin-left: 80px; color: var(--name-red); }

  /* brand name */
  .brand {
    position: absolute;
    display: flex; align-items: center; gap: 8px;
    color: var(--brand-orange);
    font-weight: 700;
    line-height: 1.02;
    text-transform: uppercase;
  }
  .brand__dot { flex: none; border-radius: 50%; background: var(--brand-orange); }
  .brand--small { left: 250px; top: 96px; font-size: 22px; }
  .brand--small .brand__dot { width: 18px; height: 18px; }
  .brand--large { left: 120px; top: 78px; font-size: 34px; }
  .brand--large .brand__dot { width: 26px; height: 26px; }
</style>
</head>
<body>
<main class="sheet">

  <!-- front, light -->
  <section class="card card--front-light">
    <div class="stroke stroke--orange-top" role="img" aria-label="Orange paint brush strokes"></div>
    <div class="stroke stroke--blue-corner" role="img" aria-label="Blue paint brush strokes"></div>
    <div class="stroke stroke--red-corner" role="img" aria-label="Red paint brush strokes"></div>
    <div class="holder">
      <p class="holder__name">Daniel Okafor</p>
      <p class="holder__title">Financial Advisor</p>
      <div class="holder__rule"></div>
    </div>
    <div class="brand brand--small"><span class="brand__dot"></span><span>Lakeshore<br>Youngsters<br>Circle</span></div>
    <div class="contact">
      <p class="contact__row"><span class="contact__label">Adress:</span>210 Harbor Lane</p>
      <p class="contact__row"><span class="contact__label">State:</span>Minnesota</p>
      <p class="contact__row"><span class="contact__label">zip code:</span>55401</p>
      <p class="contact__row"><span class="contact__label">Email:</span>d.okafor@mail.com</p>
      <p class="contact__row"><span class="contact__label">Tel:</span>02 0145 066 321 7</p>
      <p class="contact__web">www.lakeshoreyoungsters.com</p>
    </div>
  </section>

  <!-- back, light -->
  <section class="card card--back-light">
    <div class="stroke stroke--orange-top" role="img" aria-label="Orange paint brush strokes"></div>
    <div class="stroke stroke--green-corner" role="img" aria-label="Green paint brush strokes"></div>
    <div class="brand brand--large"><span class="brand__dot"></span><span>Lakeshore<br>Youngsters<br>Circle</span></div>
  </section>

  <!-- front, dark -->
  <section class="card card--dark card--front-dark">
    <div class="stroke stroke--orange-top" role="img" aria-label="Orange paint brush strokes"></div>
    <div class="stroke stroke--blue-corner" role="img" aria-label="Blue paint brush strokes"></div>
    <div class="stroke stroke--red-corner" role="img" aria-label="Red paint brush strokes"></div>
    <div class="holder">
      <p class="holder__name">Daniel Okafor</p>
      <p class="holder__title">Financial Advisor</p>
      <div class="holder__rule"></div>
    </div>
    <div class="brand brand--small"><span class="brand__dot"></span><span>Lakeshore<br>Youngsters<br>Circle</span></div>
    <div class="contact">
      <p class="contact__row"><span class="contact__label">Adress:</span>210 Harbor Lane</p>
      <p class="contact__row"><span class="contact__label">State:</span>Minnesota</p>
      <p class="contact__row"><span class="contact__label">zip code:</span>55401</p>
      <p class="contact__row"><span class="contact__label">Email:</span>d.okafor@mail.com</p>
      <p class="contact__row"><span class="contact__label">Tel:</span>02 0145 066 321 7</p>
      <p class="contact__web">www.lakeshoreyoungsters.com</p>
    </div>
  </section>

  <!-- back, dark -->
  <section class="card card--dark card--back-dark">
    <div class="stroke stroke--orange-top" role="img" aria-label="Orange paint brush strokes"></div>
    <div class="stroke stroke--green-corner" role="img" aria-label="Green paint brush strokes"></div>
    <div class="brand brand--large"><span class="brand__dot"></span><span>Lakeshore<br>Youngsters<br>Circle</span></div>
  </section>

</main>
</body>
</html>
```